R.T. Dunmore Electrical work flyer

I need a flyer design to help generate some extra work. I'm more than happy for a designer to play around with pictures, text, headings, boarders. The flyer will be double sided A4 size.
We specialize in Residential, Commercial, & Industrial Electrical works including PV Solar System Designs & Installations, Maintenance, System Checks & Upgrades, Mains Upgrades, Overhead & Underground, Switchboard Installations & Upgrades, Safety Switches, Spa & Pool connections, LED Lighting solutions, Energy Audit Checks, Fans & Air Conditioning, Hi-bay Lighting, Carpark Lighting, Data Points, Comms Racks, New Home Builds, Office Fitouts ...
We pride ourselves on always doing a great job, guaranteed workmanship, competitive pricing, & leaving the site clean.
Call Grant for a quote on any of your electrical needs
Mobile:0412 738 164
Email: rtdunmoreelectrical@mailbox-example.net
PO Box 78
Ferngrove Heights VIC 3188

REC: 38571
CEC Accreditation: B2815096

I've added my company logo & some pics, photo's & electrical / solar brand logos that can be used but not a must. I'm more than happy if you can find better pics.

Target Market(s)

Office, Factory & Home Owners

Industry/Entity Type

Electrical

Font styles to use
Serif
Sans Serif

Requirements
Must have
• eye catchy design with not to much information overload.
• Just aiming for people to call up for quotes etc.
Nice to have
• My company logo, electrical & solar works available
Should not have
• pictures of kids

```html
<!DOCTYPE html>
<html lang="en">
<head>
<meta charset="utf-8">
<title>R.T. Dunmore Electrical – Flyer</title>
<link rel="stylesheet" href="https://fonts.googleapis.com/css2?family=Archivo:wdth,wght@62..125,300..800&family=Oswald:wght@500;700&family=Open+Sans:ital,wght@0,400;0,600;0,700;1,600&display=swap">
<style>
  :root{
    --green:#5dbb2f;
    --green-dark:#3f9a1f;
    --ink:#1c1c1c;
    --band:#1f1f1f;
    --grey:#6a6a6a;
    --paper:#ffffff;
    --backdrop:#7a5235;
  }
  *{margin:0;padding:0;box-sizing:border-box}
  html,body{width:1200px;height:907px;overflow:hidden;background:var(--backdrop)}
  .canvas{position:relative;width:1200px;height:907px}
  .page{position:absolute;top:68px;height:767px;background:var(--paper);overflow:hidden;box-shadow:0 4px 14px rgba(0,0,0,.35)}
  .page--front{left:44px;width:540px}
  .page--back{left:615px;width:548px}
  .abs{position:absolute}
  .wide{font-family:"Archivo",Arial,sans-serif;font-stretch:125%}
  .photo{position:absolute}
  .round{border-radius:50%;border:4px solid #fff;box-shadow:0 2px 6px rgba(0,0,0,.35)}

  .brand{position:absolute;display:flex;align-items:center;gap:8px;font-family:"Archivo",Arial,sans-serif;font-weight:400;font-size:18px;line-height:20px}
  .brand__dot{width:34px;height:34px;border-radius:50%;background:var(--green);flex:none}

  .headline{left:23px;top:277px;font-size:27px;font-weight:800;color:var(--green);letter-spacing:.5px}
  .sub-light{left:23px;top:309px;font-size:11.2px;font-weight:300;color:var(--grey);letter-spacing:.6px}
  .sub-bold{left:23px;top:324px;font-size:11.6px;font-weight:700;color:#333}
  .tab{left:0;top:350px;width:121px;height:18px;background:var(--green);border-radius:0 9px 9px 0;font-size:12.5px;font-weight:800;color:var(--ink);padding-left:22px;line-height:18px}

  .services{position:absolute;top:375px;list-style:none;font-family:"Open Sans",Arial,sans-serif;font-style:italic;font-weight:600;font-size:8.4px;color:#222}
  .services li{display:flex;gap:5px;min-height:14.3px;line-height:10px}
  .services li.two-line{min-height:25px}
  .services svg{flex:none;margin-top:1px}
  .services--a{left:22px}
  .services--b{left:206px}

  .strip{position:absolute;top:608px;height:6px;background:var(--green)}
  .band{position:absolute;top:618px;height:102px;background:var(--band);color:#fff;font-family:"Open Sans",Arial,sans-serif}
  .band__call{position:absolute;left:25px;top:12px;font-size:10px;font-weight:700;color:var(--green);line-height:12.5px;letter-spacing:.4px}
  .contact{position:absolute;font-size:9px;line-height:12.5px;display:flex;gap:5px;white-space:nowrap}
  .contact svg{flex:none;margin-top:2px}
  .cred{position:absolute;font-weight:700;color:var(--green);white-space:nowrap}
  .cred b{color:#fff}

  .rule{position:absolute;left:0;right:0;top:722px;height:2px;background:var(--green)}
  .partners{position:absolute;left:18px;right:18px;top:731px;display:flex;justify-content:space-between;align-items:center}
  .partners span{display:block;height:12px;background:#d8d8d8;border-radius:2px}

  .about-title{right:20px;top:300px;font-size:19px;font-weight:800;color:var(--green)}
  .about-copy{left:213px;top:327px;width:318px;font-family:"Open Sans",Arial,sans-serif;font-size:8.3px;line-height:11.4px;color:#222;text-align:justify}
  .call-now{left:17px;top:516px;font-family:"Oswald",Arial,sans-serif;font-weight:700;font-size:42px;color:var(--green);line-height:48px;transform:scaleX(.7);transform-origin:left top;white-space:nowrap}
  .call-num{left:20px;top:564px;font-family:"Oswald",Arial,sans-serif;font-weight:500;font-size:26px;color:#111;line-height:30px;transform:scaleX(.84);transform-origin:left top;white-space:nowrap}
</style>
</head>
<body>
<div class="canvas">

  <!-- FRONT -->
  <section class="page page--front">
    <div class="photo" role="img" aria-label="Faint rows of solar panels" style="left:180px;top:0;width:360px;height:260px;background:linear-gradient(200deg,#d9dcde,#f4f5f6 60%,#fff)"></div>
    <div class="photo" role="img" aria-label="Light bulb containing solar panels under a blue sky" style="left:26px;top:22px;width:310px;height:190px;border-radius:50% 40% 40% 50%;background:radial-gradient(circle at 40% 40%,#9fd0f2,#3f7fc4 60%,#8c8f92 100%)"></div>
    <svg class="abs" style="left:0;top:0" width="540" height="300" viewBox="0 0 540 300" aria-hidden="true">
      <path d="M0,205 C150,262 380,232 498,66 L474,50 L538,26 L531,96 L510,80 C390,255 160,298 0,238 Z" fill="var(--green)"/>
    </svg>
    <div class="brand" style="left:345px;top:219px;color:#555">
      <span class="brand__dot"></span><span>R.T. Dunmore<br>Electrical</span>
    </div>

    <div class="photo" role="img" aria-label="Faded office interior" style="left:200px;top:270px;width:340px;height:200px;background:linear-gradient(90deg,#fff,#eeeeee)"></div>
    <h1 class="abs wide headline">WE SPECIALIZE IN</h1>
    <p class="abs wide sub-light">RESIDENTIAL,COMMERCIAL,&amp;INDUSTRIAL</p>
    <p class="abs wide sub-bold">ELECTRICAL WORKS INCLUDING PV SOLAR SYSTEM</p>
    <div class="abs wide tab">INCLUDING</div>

    <ul class="services services--a">
      <li><svg width="9" height="7" viewBox="0 0 9 7"><path d="M1 3.5l2.5 2.5L8 1" stroke="var(--green)" stroke-width="1.8" fill="none"/></svg>PV Solar Systems</li>
      <li><svg width="9" height="7" viewBox="0 0 9 7"><path d="M1 3.5l2.5 2.5L8 1" stroke="var(--green)" stroke-width="1.8" fill="none"/></svg>Designs &amp; Installations</li>
      <li><svg width="9" height="7" viewBox="0 0 9 7"><path d="M1 3.5l2.5 2.5L8 1" stroke="var(--green)" stroke-width="1.8" fill="none"/></svg>Maintenance</li>
      <li><svg width="9" height="7" viewBox="0 0 9 7"><path d="M1 3.5l2.5 2.5L8 1" stroke="var(--green)" stroke-width="1.8" fill="none"/></svg>System Checks &amp; Upgrades</li>
      <li><svg width="9" height="7" viewBox="0 0 9 7"><path d="M1 3.5l2.5 2.5L8 1" stroke="var(--green)" stroke-width="1.8" fill="none"/></svg>Mains Upgrades</li>
      <li><svg width="9" height="7" viewBox="0 0 9 7"><path d="M1 3.5l2.5 2.5L8 1" stroke="var(--green)" stroke-width="1.8" fill="none"/></svg>Overhead &amp; Underground</li>
      <li class="two-line"><svg width="9" height="7" viewBox="0 0 9 7"><path d="M1 3.5l2.5 2.5L8 1" stroke="var(--green)" stroke-width="1.8" fill="none" opacity="0"/></svg><span>Switchboard Installations<br>&amp; Upgrades</span></li>
      <li><svg width="9" height="7" viewBox="0 0 9 7"><path d="M1 3.5l2.5 2.5L8 1" stroke="var(--green)" stroke-width="1.8" fill="none"/></svg>Safety Switches</li>
    </ul>
    <ul class="services services--b">
      <li><svg width="9" height="7" viewBox="0 0 9 7"><path d="M1 3.5l2.5 2.5L8 1" stroke="var(--green)" stroke-width="1.8" fill="none"/></svg>LED Lighting solutions</li>
      <li><svg width="9" height="7" viewBox="0 0 9 7"><path d="M1 3.5l2.5 2.5L8 1" stroke="var(--green)" stroke-width="1.8" fill="none"/></svg>Energy Audit Checks</li>
      <li><svg width="9" height="7" viewBox="0 0 9 7"><path d="M1 3.5l2.5 2.5L8 1" stroke="var(--green)" stroke-width="1.8" fill="none"/></svg>Fans &amp; Air Conditioning</li>
      <li><svg width="9" height="7" viewBox="0 0 9 7"><path d="M1 3.5l2.5 2.5L8 1" stroke="var(--green)" stroke-width="1.8" fill="none"/></svg>HI-bay Lighting</li>
      <li><svg width="9" height="7" viewBox="0 0 9 7"><path d="M1 3.5l2.5 2.5L8 1" stroke="var(--green)" stroke-width="1.8" fill="none"/></svg>Carpark Lighting</li>
      <li><svg width="9" height="7" viewBox="0 0 9 7"><path d="M1 3.5l2.5 2.5L8 1" stroke="var(--green)" stroke-width="1.8" fill="none"/></svg>Data Points</li>
      <li><svg width="9" height="7" viewBox="0 0 9 7"><path d="M1 3.5l2.5 2.5L8 1" stroke="var(--green)" stroke-width="1.8" fill="none"/></svg>Comms Racks</li>
      <li><svg width="9" height="7" viewBox="0 0 9 7"><path d="M1 3.5l2.5 2.5L8 1" stroke="var(--green)" stroke-width="1.8" fill="none"/></svg>New Home Builds</li>
      <li><svg width="9" height="7" viewBox="0 0 9 7"><path d="M1 3.5l2.5 2.5L8 1" stroke="var(--green)" stroke-width="1.8" fill="none"/></svg>Spa &amp; Pool connections</li>
      <li><svg width="9" height="7" viewBox="0 0 9 7"><path d="M1 3.5l2.5 2.5L8 1" stroke="var(--green)" stroke-width="1.8" fill="none"/></svg>Office Fitouts</li>
    </ul>

    <svg class="abs" style="left:376px;top:450px" width="164" height="317" viewBox="376 450 164 317" role="img" aria-label="Open switchboard with rows of circuit breakers">
      <defs><linearGradient id="boardTone" x1="0" y1="0" x2="1" y2="1"><stop offset="0" stop-color="#e9ecee"/><stop offset=".55" stop-color="#a9adb0"/><stop offset="1" stop-color="#5d6266"/></linearGradient></defs>
      <path d="M540,450 C450,470 400,530 385,610 L385,767 L540,767 Z" fill="var(--green)"/>
      <path d="M540,463 C460,483 407,540 396,615 L396,767 L540,767 Z" fill="url(#boardTone)"/>
    </svg>

    <div class="photo round" role="img" aria-label="Warehouse with hi-bay lighting" style="left:24px;top:532px;width:82px;height:82px;background:radial-gradient(circle at 50% 35%,#eef3f7,#8c99a6 70%,#4d5863)"></div>
    <div class="photo round" role="img" aria-label="Factory floor lit by LED fittings" style="left:130px;top:532px;width:82px;height:82px;background:radial-gradient(circle at 50% 35%,#f3f5f7,#96a1ab 70%,#505a63)"></div>
    <div class="photo round" role="img" aria-label="Pool lit in blue and purple" style="left:236px;top:532px;width:82px;height:82px;background:radial-gradient(circle at 50% 45%,#a98cff,#3a2aa8 65%,#120d3d)"></div>

    <div class="strip" style="left:0;width:385px"></div>
    <div class="band" style="left:0;width:390px">
      <p class="band__call wide">CALL GRANT FOR A QUOTE ON ANY<br>OF YOUR ELECTRICAL NEEDS</p>
      <div class="contact" style="left:25px;top:38px"><svg width="7" height="10" viewBox="0 0 7 10"><path d="M3.5 0A3.5 3.5 0 0 0 0 3.5C0 6 3.5 10 3.5 10S7 6 7 3.5A3.5 3.5 0 0 0 3.5 0Zm0 5a1.4 1.4 0 1 1 0-2.8 1.4 1.4 0 0 1 0 2.8Z" fill="var(--green)"/></svg><span>PO Box 78<br>Ferngrove Heights VIC 3188</span></div>
      <div class="contact" style="left:25px;top:63px"><svg width="8" height="8" viewBox="0 0 8 8"><path d="M1.6 0l1.5 2-1 1c.6 1.2 1.5 2.1 2.7 2.7l1-1L8 6.2 6.8 8C3 7.6.4 5 0 1.2Z" fill="var(--green)"/></svg><span>0412 738 164</span></div>
      <div class="contact" style="left:25px;top:76px;font-size:8px"><svg width="9" height="7" viewBox="0 0 9 7"><rect width="9" height="7" rx="1" fill="var(--green)"/><path d="M.5.8 4.5 4l4-3.2" stroke="var(--band)" fill="none"/></svg><span>rtdunmoreelectrical@mailbox-example.net</span></div>
      <p class="cred" style="left:232px;top:62px;font-size:9px">REC: <b>38571</b></p>
      <p class="cred" style="left:232px;top:76px;font-size:9px">CEC Accreditation: <b>B2815096</b></p>
    </div>
    <div class="rule"></div>
    <div class="partners" aria-label="Partner brands">
      <span style="width:36px"></span><span style="width:38px"></span><span style="width:28px"></span><span style="width:44px"></span><span style="width:36px"></span><span style="width:30px"></span><span style="width:14px"></span><span style="width:20px"></span>
    </div>
  </section>

  <!-- BACK -->
  <section class="page page--back">
    <div class="photo" role="img" aria-label="Bright open-plan office with rows of desks" style="left:0;top:0;width:548px;height:290px;background:linear-gradient(180deg,#f7f8f9,#d8dcdf 55%,#9ea4a9)"></div>
    <svg class="abs" style="left:0;top:0" width="548" height="380" viewBox="0 0 548 380" aria-hidden="true">
      <path d="M0,0 L40,0 C90,150 260,262 548,250 L548,292 C380,300 250,275 140,290 C80,298 30,330 0,372 Z" fill="var(--band)"/>
      <path d="M548,216 C330,232 150,190 46,58 L28,72 L6,2 L76,24 L60,38 C160,165 330,206 548,200 Z" fill="var(--green)"/>
    </svg>
    <div class="brand" style="left:25px;top:206px;color:#fff">
      <span class="brand__dot"></span><span>R.T. Dunmore<br>Electrical</span>
    </div>

    <div class="photo" role="img" aria-label="Electrical distribution board on a wall" style="left:0;top:300px;width:140px;height:210px;background:linear-gradient(180deg,#eef0f1,#c6cacd 60%,#8f959a)"></div>
    <svg class="abs" style="left:0;top:250px" width="200" height="300" viewBox="0 250 200 300" aria-hidden="true">
      <path d="M70,270 C110,330 150,420 158,520" stroke="var(--green)" stroke-width="13" fill="none"/>
    </svg>
    <div class="photo round" role="img" aria-label="Large warehouse with rows of hi-bay lights" style="left:71px;top:256px;width:126px;height:126px;background:radial-gradient(circle at 50% 30%,#f4f7fa,#8f9ba6 65%,#47525c)"></div>

    <h2 class="abs wide about-title">About us</h2>
    <p class="abs about-copy">Lorem Ipsum is simply dummy text of the printing and typesetting industry. Lorem Ipsum has been the industry's standard dummy text ever since the 1500s, when an unknown printer took a galley of type and scrambled it to make a type specimen book. It has survived not only five centuries, but also the leap into electronic typesetting, remaining essentially unchanged. It was popularised in the 1960s with the release of Typeline sheets containing Lorem Ipsum passages, and more recently with desktop publishing software like Quillset PageBuilder including Contrary to popular belief, Lorem Ipsum is not simply random text. It has roots in a piece of classical Latin literature from 45 BC, making it over 2000 years old. Harold Pemberton, a Latin professor at Westbrook College in Ohio, looked up one of the more obscure Latin words, consectetur, from a Lorem Ipsum passage, and going through the cites of the word in classical literature, discovered the undoubtable source.versions of Lorem Ipsum.</p>

    <p class="abs call-now">CALL NOW</p>
    <p class="abs call-num">0412 738 164</p>

    <div class="photo round" role="img" aria-label="Living room with warm downlights" style="left:155px;top:501px;width:118px;height:118px;background:radial-gradient(circle at 50% 40%,#f1e6d6,#9b8772 65%,#3e3329)"></div>
    <div class="photo round" role="img" aria-label="Modern lounge with white sofas" style="left:275px;top:501px;width:118px;height:118px;background:radial-gradient(circle at 50% 40%,#ffffff,#c9c6c1 60%,#6e6b66)"></div>
    <div class="photo round" role="img" aria-label="Spa water lit in blue" style="left:417px;top:501px;width:118px;height:118px;background:radial-gradient(circle at 50% 45%,#8fe2ff,#1f7fd1 60%,#0a2a5a)"></div>

    <div class="strip" style="left:0;width:548px"></div>
    <div class="band" style="left:0;width:548px">
      <p class="band__call wide" style="left:27px">CALL GRANT FOR A QUOTE ON ANY<br>OF YOUR ELECTRICAL NEEDS</p>
      <div class="contact" style="left:28px;top:56px;font-size:10px"><svg width="7" height="10" viewBox="0 0 7 10"><path d="M3.5 0A3.5 3.5 0 0 0 0 3.5C0 6 3.5 10 3.5 10S7 6 7 3.5A3.5 3.5 0 0 0 3.5 0Zm0 5a1.4 1.4 0 1 1 0-2.8 1.4 1.4 0 0 1 0 2.8Z" fill="var(--green)"/></svg><span>PO Box 78<br>Ferngrove Heights VIC 3188</span></div>
      <div class="contact" style="left:195px;top:56px;font-size:10px"><svg width="10" height="10" viewBox="0 0 10 10"><rect width="10" height="10" rx="2" fill="var(--green)"/><path d="M3 2l1.2 1.6-.8.8c.5 1 1.2 1.7 2.2 2.2l.8-.8L8 7 7 8.3C4.3 8 2 5.7 1.7 3Z" fill="var(--band)"/></svg><span>0412 738 164</span></div>
      <div class="contact" style="left:195px;top:72px;font-size:9.5px"><svg width="11" height="8" viewBox="0 0 11 8"><rect width="11" height="8" rx="1" fill="var(--green)"/><path d="M.6.8 5.5 4.6 10.4.8" stroke="var(--band)" fill="none"/></svg><span>rtdunmoreelectrical@mailbox-example.net</span></div>
      <p class="cred" style="left:368px;top:28px;font-size:12px">REC: <b>38571</b></p>
      <p class="cred" style="left:368px;top:45px;font-size:12px">CEC Accreditation: <b>B2815096</b></p>
    </div>
    <div class="rule"></div>
    <div class="partners" aria-label="Partner brands" style="left:30px;right:20px">
      <span style="width:36px"></span><span style="width:40px"></span><span style="width:30px"></span><span style="width:44px"></span><span style="width:38px"></span><span style="width:34px"></span><span style="width:14px"></span><span style="width:20px"></span>
    </div>
  </section>

</div>
</body>
</html>
```